International Sex Coach needs a Book Cover in less than 3 days

I need a cover design for my book coming out next week titled "The Open Map of Desire". The book explores the origins of our cultural ideas about sexuality and taboo and is interwoven with personal memoir.
The reader must feel that they are being pulled into an intimate sexual story, but also a deeper understanding of sex itself. Like they are jumping into bed with me, you might say. I would like the title to take up the majority of the space over an image of 3D, very real bed sheets, but I am open to your ideas. I haven't purchased any images yet, but there are a few below I was drawn to.
In its essence, this book is designed to reeducate the reader about sexuality and open them up to a new paradigm of sexual wellness.
The author name is Marisa Tolven. Page must also include the phrase: a revolutionary new approach to sexuality, relationship and love.
Size 6" x 9" (15.24 x 22.86 cm)
Thanks!
Updates

Target Market(s)

Sexually active men and women.

Industry/Entity Type

Wellness

Font styles to use
Serif

```html
<!DOCTYPE html>
<html lang="en">
<head>
<meta charset="utf-8">
<title>The Open Map of Desire — Marisa Tolven</title>
<link rel="stylesheet" href="https://fonts.googleapis.com/css2?family=Oswald:wght@400;500;600&display=swap">
<style>
  :root {
    --ink: #0b0b0b;
    --night: #000000;
    --sheet: #f1efec;
    --sheet-shadow: #d6d1cb;
    --skin: #b88f7b;
    --rose: #ec2860;
    --white: #ffffff;
  }
  * { margin: 0; padding: 0; box-sizing: border-box; }
  html, body {
    width: 800px;
    height: 1200px;
    overflow: hidden;
    background: var(--night);
  }
  .cover {
    position: relative;
    width: 800px;
    height: 1200px;
    overflow: hidden;
    font-family: "Oswald", sans-serif;
    text-transform: uppercase;
  }
  .cover-photo {
    position: absolute;
    inset: 0;
    width: 800px;
    height: 1200px;
  }
  .title-lead {
    position: absolute;
    top: 19px;
    left: 0;
    width: 100%;
    text-align: center;
    font-weight: 500;
    font-size: 64px;
    line-height: 64px;
    letter-spacing: 2px;
    color: var(--white);
    white-space: nowrap;
  }
  .title-lead .accent { color: var(--rose); }
  .title-main {
    position: absolute;
    top: 110px;
    left: 0;
    width: 100%;
    text-align: center;
    font-weight: 500;
    font-size: 234px;
    line-height: 234px;
    letter-spacing: 6px;
    color: var(--rose);
    white-space: nowrap;
  }
  .tagline {
    position: absolute;
    top: 971px;
    left: 20px;
    width: 760px;
    text-align: center;
    font-weight: 400;
    font-size: 46px;
    line-height: 44px;
    letter-spacing: 1px;
    color: var(--ink);
  }
  .author {
    position: absolute;
    top: 1070px;
    left: 0;
    width: 100%;
    text-align: center;
    font-weight: 500;
    font-size: 58px;
    line-height: 58px;
    letter-spacing: 2px;
    color: var(--rose);
  }
</style>
</head>
<body>
  <main class="cover">
    <svg class="cover-photo" viewBox="0 0 800 1200" role="img" aria-label="Photograph of two clasped hands resting on white bed sheets against a black background">
      <defs>
        <linearGradient id="sheetLight" x1="0" y1="0" x2="0" y2="1">
          <stop offset="0" stop-color="#000000"/>
          <stop offset="0.36" stop-color="#000000"/>
          <stop offset="0.5" stop-color="#2a2220"/>
          <stop offset="0.58" stop-color="#d6d1cb"/>
          <stop offset="0.68" stop-color="#f1efec"/>
          <stop offset="1" stop-color="#efece8"/>
        </linearGradient>
        <radialGradient id="handsGlow" cx="0.45" cy="0.5" r="0.55">
          <stop offset="0" stop-color="#b88f7b" stop-opacity="0.7"/>
          <stop offset="1" stop-color="#b88f7b" stop-opacity="0"/>
        </radialGradient>
      </defs>
      <rect width="800" height="1200" fill="url(#sheetLight)"/>
      <rect x="0" y="400" width="700" height="390" fill="url(#handsGlow)"/>
    </svg>

    <h1 class="title">
      <span class="title-lead">The <span class="accent">Open Map</span> of</span>
      <span class="title-main">Desire</span>
    </h1>

    <p class="tagline">A revolutionary new approach to sexuality, relationship and love.</p>

    <p class="author">Marisa Tolven</p>
  </main>
</body>
</html>
```